Build Distinctive Business Card: Public Relations Government Relations firm

I have logo and colors done (attached) need a very cool way to present it on a business card (can be two sided if need be).

Public Relations Government Relations firm

Info:

Mark Tillson, CEO
Keystone Public Relations
2786 West Harlow Blvd.
Los Angeles CA 90047
(o) 213.555.0148
(f) 213.555.0193
mark@keystonekpr-example.com

Target Market(s)

Government relations, public relations, lobbyist, I was a past State Senator

Industry/Entity Type

Business

Contact Information for Business Card

Info:

Mark Tillson, CEO
Keystone Public Relations
2786 West Harlow Blvd.
Los Angeles CA 90047
(o) 213.555.0148
(f) 213.555.0193
mark@keystonekpr-example.com
@marktillson

Requirements
Must have
• A sense of balance given logo is already done.
• It's a government relations firm really.
• Lobbyist type.
• Senatorial type...

```html
<!DOCTYPE html>
<html lang="en">
<head>
<meta charset="UTF-8">
<title>Keystone Public Relations – Business Card</title>
<link href="https://fonts.googleapis.com/css2?family=Open+Sans:wght@400;600&display=swap" rel="stylesheet">
<style>
  :root {
    --backdrop: #2b2624;
    --card: #151617;
    --blue: #1e8fcf;
    --blue-dark: #13628f;
    --white: #f2f2f2;
    --grey: #8a8d90;
  }
  * { margin: 0; padding: 0; box-sizing: border-box; }
  html, body {
    width: 1200px;
    height: 716px;
    overflow: hidden;
    background: var(--backdrop);
    font-family: "Open Sans", Arial, sans-serif;
  }
  .stage {
    width: 1200px;
    height: 716px;
    display: flex;
    align-items: center;
    justify-content: center;
    gap: 48px;
  }
  .card {
    width: 525px;
    height: 300px;
    background: var(--card);
    border-radius: 4px;
    position: relative;
    overflow: hidden;
    box-shadow: 0 14px 30px rgba(0,0,0,.45);
  }

  /* Front side */
  .card--front {
    display: flex;
    flex-direction: column;
    align-items: center;
    justify-content: center;
  }
  .brand-mark {
    width: 96px;
    height: 96px;
    border-radius: 50%;
    background: var(--blue);
    margin-bottom: 14px;
  }
  .brand-name {
    color: var(--blue);
    font-size: 54px;
    font-weight: 400;
    line-height: 1;
    letter-spacing: 1px;
  }
  .brand-tagline {
    color: var(--grey);
    font-size: 11px;
    letter-spacing: 4px;
    margin-top: 8px;
    text-transform: uppercase;
  }

  /* Back side */
  .back-ring {
    position: absolute;
    left: -40px;
    top: 40px;
    width: 230px;
    height: 230px;
    border-radius: 50%;
    border: 10px solid var(--blue);
  }
  .contact {
    position: absolute;
    right: 32px;
    top: 52px;
    text-align: right;
    color: var(--white);
  }
  .contact__name {
    color: var(--blue);
    font-size: 30px;
    font-weight: 400;
    line-height: 1.1;
  }
  .contact__title {
    font-size: 13px;
    margin-top: 2px;
  }
  .contact__company {
    font-size: 13px;
  }
  .contact__list {
    list-style: none;
    text-align: left;
    margin-top: 20px;
    margin-left: auto;
    width: 232px;
    font-size: 13px;
    line-height: 1.45;
  }
  .contact__item {
    display: flex;
    gap: 10px;
    margin-bottom: 4px;
  }
  .contact__icon {
    width: 12px;
    height: 12px;
    flex: none;
    margin-top: 3px;
    fill: var(--white);
  }
</style>
</head>
<body>
<main class="stage">
  <section class="card card--front" aria-label="Card front">
    <div class="brand-mark" aria-hidden="true"></div>
    <div class="brand-name">Keystone</div>
    <div class="brand-tagline">Public Relations</div>
  </section>

  <section class="card card--back" aria-label="Card back">
    <div class="back-ring" aria-hidden="true"></div>
    <div class="contact">
      <div class="contact__name">Mark Tillson</div>
      <div class="contact__title">CEO</div>
      <div class="contact__company">Keystone Public Relations</div>
      <ul class="contact__list">
        <li class="contact__item">
          <svg class="contact__icon" viewBox="0 0 12 12" aria-hidden="true"><path d="M6 0a4 4 0 0 0-4 4c0 3 4 8 4 8s4-5 4-8a4 4 0 0 0-4-4zm0 5.5A1.5 1.5 0 1 1 6 2.5a1.5 1.5 0 0 1 0 3z"/></svg>
          <span>2786 West Harlow Blvd.<br>Los Angeles CA 90047</span>
        </li>
        <li class="contact__item">
          <svg class="contact__icon" viewBox="0 0 12 12" aria-hidden="true"><path d="M1 3c0-1 2-2 5-2s5 1 5 2v1H8V3H4v1H1zM3 5h6l2 3v3H1V8zm3 1.3a1.5 1.5 0 1 0 0 3 1.5 1.5 0 0 0 0-3z"/></svg>
          <span>213.555.0148<br>213.555.0193</span>
        </li>
        <li class="contact__item">
          <svg class="contact__icon" viewBox="0 0 12 12" aria-hidden="true"><path d="M0 2h12v8H0zm1 1v.4l5 3.3 5-3.3V3zm0 1.6V9h10V4.6L6 7.9z"/></svg>
          <span>mark@keystonekpr-example.com</span>
        </li>
      </ul>
    </div>
  </section>
</main>
</body>
</html>
```